We need a business card design for an Afghan catering business called 'Velmi Catering'. We provide Afghan food for any occasions such as wedding, birthday, engagement, small gathering, etc. We would like the business card to include the name of the business designed with the logo, phone number, and the address. We already have our logo that we would upload. The design that we require or suggest must be black with the logo and if possible change the colors of the logo (e.g. the logo includes red and gray lines) to gold. In other words, we would like the business card color to be black with some luxury design that would match the logo. For the front, we would like the logo which includes the name of the business, contact info, and the address. Also, depending on the design we would like to include some pictures of the food. the location (map), facebook, and instagram. After having a look at the design of the business card, we also need menu design and flyer design same thing as the business card design.

Industry/Entity Type

Business

Contact Information for Business Card

Title: Velmi Catering
Phone #: 5550142863 and 5550197214
Name: Lutfiya

Font styles to use
Serif
Script

Colors
000000

Requirements
Must have
• My project must have the name (with the logo), phone number, email, name, address, map, a few picture of the food, facebook, and Instagram logo.
Nice to have
• The color and font must match the logo. It must look simple and luxury (with suggested color black).

```html
<!DOCTYPE html>
<html lang="en">
<head>
<meta charset="utf-8">
<title>Velmi Catering — Business Card</title>
<link href="https://fonts.googleapis.com/css2?family=Cormorant+Garamond:wght@500;600;700&family=Great+Vibes&display=swap" rel="stylesheet">
<style>
  :root {
    --page-bg: #ececec;
    --card-bg: #000000;
    --card-edge: #1a1a1a;
    --gold: #c9a24a;
    --gold-light: #e6c878;
    --ink: #e9e2d0;
    --map-land: #2a2620;
    --map-water: #3d3a33;
    --food-warm: #c8742c;
    --food-deep: #8a3a17;
    --food-green: #6f8f3a;
  }
  * { box-sizing: border-box; margin: 0; padding: 0; }
  html, body {
    width: 1200px; height: 900px; overflow: hidden;
    background: var(--page-bg);
    font-family: "Cormorant Garamond", Georgia, serif;
    color: var(--ink);
  }
  .stage {
    width: 1200px; height: 900px;
    display: flex; align-items: center; justify-content: center; gap: 48px;
  }
  .card {
    width: 520px; height: 298px;
    background: var(--card-bg);
    box-shadow: 0 10px 26px rgba(0,0,0,.22);
    position: relative; overflow: hidden;
  }
  .card-front {
    padding: 30px 36px;
    border: 1px solid var(--card-edge);
  }
  .card-front::after {
    content: ""; position: absolute; inset: 10px;
    border: 1px solid rgba(201,162,74,.45); pointer-events: none;
  }
  .holder-name {
    color: var(--gold); font-weight: 700; font-size: 22px; letter-spacing: 2px;
  }
  .holder-title {
    font-family: "Great Vibes", cursive;
    font-size: 20px; color: var(--gold-light); line-height: 1; margin-top: 2px;
  }
  .social-row { display: flex; gap: 14px; margin-top: 18px; }
  .social-mark { width: 14px; height: 14px; background: var(--gold); border-radius: 2px; }
  .contact-list { list-style: none; margin-top: 12px; font-size: 15px; font-weight: 600; }
  .contact-list li { display: flex; align-items: center; gap: 10px; margin-bottom: 4px; }
  .contact-list svg { width: 12px; height: 12px; flex: none; }
  .location-map {
    position: absolute; left: 36px; bottom: 26px;
    width: 128px; height: 62px;
    border: 1px solid var(--gold);
    background: linear-gradient(135deg, var(--map-land) 0 55%, var(--map-water) 55% 100%);
  }
  .brand {
    position: absolute; right: 40px; top: 124px;
    display: flex; align-items: center; gap: 10px;
  }
  .brand-dot { width: 26px; height: 26px; border-radius: 50%; background: var(--gold); }
  .brand-name { color: var(--gold); font-weight: 700; font-size: 30px; letter-spacing: .5px; }
  .address {
    position: absolute; right: 40px; bottom: 26px;
    text-align: right; font-size: 15px; font-weight: 600; line-height: 1.3;
    font-style: normal;
  }
  .card-back .food-photo {
    width: 100%; height: 100%;
    background:
      linear-gradient(115deg, var(--food-green) 0 22%, transparent 22%),
      linear-gradient(60deg, var(--food-deep) 0%, var(--food-warm) 45%, #d99a45 70%, var(--food-deep) 100%);
  }
</style>
</head>
<body>
<main class="stage">
  <section class="card card-front">
    <h1 class="holder-name">DORIAN KELLER</h1>
    <p class="holder-title">Director</p>
    <div class="social-row">
      <span class="social-mark" aria-label="Social profile"></span>
      <span class="social-mark" aria-label="Social profile"></span>
    </div>
    <ul class="contact-list">
      <li>
        <svg viewBox="0 0 12 12"><rect x="3" y="0.5" width="6" height="11" rx="1" fill="none" stroke="var(--gold)" stroke-width="1.2"/><circle cx="6" cy="9.5" r=".7" fill="var(--gold)"/></svg>
        +61-400 555 018
      </li>
      <li>
        <svg viewBox="0 0 12 12"><rect x="0.5" y="2" width="11" height="8" fill="var(--gold)"/><path d="M0.5 2 6 6.5 11.5 2" fill="none" stroke="#000" stroke-width="1"/></svg>
        info@velmicatering.com
      </li>
    </ul>
    <div class="location-map" role="img" aria-label="Small location map showing the Larkfield area"></div>
    <div class="brand">
      <span class="brand-dot"></span>
      <span class="brand-name">Velmi Catering</span>
    </div>
    <address class="address">
      PO Box 482<br>Larkfield<br>NSW 2999 AUSTRALIA
    </address>
  </section>
  <section class="card card-back">
    <div class="food-photo" role="img" aria-label="Collage of Afghan catered dishes: salads, grilled meats and vegetables in serving trays"></div>
  </section>
</main>
</body>
</html>
```